Pura Senda Trek Holidays Rack Card

We need a double sided rack card design. One side should be promoting our "Seven Trail Days" tour with the flip side promoting our "Honeymoon" and "Custom & Family Tours". Colours should be in line with our website www.PuraSendaTrek.example. Text and photos attached (feel free to use as necessary). We are looking for a fun rack card that will catch clients eyes and hopefully promote Costa Rica as a fun and exciting vacation.

Target Market(s)

Tourism - USA and Canada

Industry/Entity Type

Tourism

Font styles to use
Sans Serif

Colors
0455a3
33a6d7
f37122

Requirements
Must have
• Our logo on both sides of the rack card. Must be bright and fun looking. Costa Rica is an outdoor destination with tons of fun activities to do, we want to try and get that feeling across on the card.
Nice to have
• I have added a price sticker to the attachments on this project. Is it possible to have something similar on the Seven Trail Days side? The price would be $1999 scored out with the new price being $1649.

```html
<!DOCTYPE html>
<html lang="en">
<head>
<meta charset="utf-8">
<title>Pura Senda Trek Holidays Rack Card</title>
<link href="https://fonts.googleapis.com/css2?family=Open+Sans:wght@400;600;700;800&display=swap" rel="stylesheet">
<style>
:root{
  --navy:#0455a3;
  --sky:#33a6d7;
  --orange:#f37122;
  --royal:#2a5ca8;
  --grey:#555a60;
  --backdrop:#d5e49c;
  --plum:#6f5358;
  --white:#ffffff;
}
*{box-sizing:border-box;margin:0;padding:0}
html,body{width:1200px;height:1000px;overflow:hidden}
body{background:var(--backdrop);font-family:"Open Sans",Arial,sans-serif;position:relative}
.card{position:absolute;background:var(--white);overflow:hidden;box-shadow:0 1px 3px rgba(0,0,0,.15)}
.card--front{left:186px;top:40px;width:424px;height:920px}
.card--back{left:626px;top:38px;width:426px;height:924px}
.abs{position:absolute}

/* front */
.hero{left:0;top:0;width:424px;height:165px;background:linear-gradient(100deg,#6c7a3c 0%,#3f4a34 35%,#7c8a88 65%,#4d5a4a 100%)}
.hero-title{left:0;top:28px;width:424px;text-align:center;color:var(--white);font-weight:800;line-height:.95;text-transform:uppercase;
  text-shadow:2px 2px 0 var(--navy),-2px -2px 0 var(--navy),2px -2px 0 var(--navy),-2px 2px 0 var(--navy)}
.hero-title .small{font-size:46px;display:block}
.hero-title .big{font-size:56px;display:block;color:var(--sky);text-shadow:2px 2px 0 var(--white),-2px -2px 0 var(--white),2px -2px 0 var(--white),-2px 2px 0 var(--white)}
.wave{left:0;width:100%}
.tagline{left:0;top:170px;width:424px;text-align:center;font-size:19px;letter-spacing:1.5px;color:var(--sky)}
.tagline .mid{color:var(--orange)}
.tagline .end{color:var(--navy)}
.tagline .dot{color:var(--orange);font-size:14px;margin:0 8px;vertical-align:2px}
.tile-photo{position:absolute}
.tile-cap{position:absolute;color:var(--white);font-size:13.5px;line-height:1.25;text-align:center;display:flex;align-items:center;justify-content:center;padding:0 6px}
.tile-cap b{font-weight:700;font-size:14px}
.tile-cap.small{font-size:11px}
.tile-cap.small b{font-size:11px}
.badge{position:absolute;width:22px;height:24px;color:var(--white);font-weight:700;font-size:16px;text-align:center;line-height:24px}
.bg-sky{background:var(--sky)}.bg-orange{background:var(--orange)}.bg-royal{background:var(--royal)}
.pitch{left:21px;top:720px;width:262px;font-size:15.5px;font-weight:700;color:var(--grey);line-height:1.3;text-align:justify;text-align-last:left}
.pitch .hl{color:var(--sky);font-size:16.5px}
.sticker{left:290px;top:712px;width:118px;height:118px;border-radius:50%;background:var(--orange);color:var(--white);text-align:center;transform:rotate(-12deg);box-shadow:2px 3px 4px rgba(0,0,0,.25);z-index:5}
.sticker .old{position:absolute;top:20px;left:0;width:100%;font-size:15px;text-decoration:line-through;color:#ffe3d2}
.sticker .only{position:absolute;top:38px;left:0;width:100%;font-size:20px;font-weight:800}
.sticker .price{position:absolute;top:60px;left:0;width:100%;font-size:29px;font-weight:800;line-height:1.2}
.brand{font-size:24px;font-weight:400;color:var(--orange);letter-spacing:1px}
.brand-dot{display:inline-block;width:12px;height:12px;border-radius:50%;background:var(--sky);margin-left:8px;vertical-align:2px}
.contact{text-align:right}
.contact .phone{font-size:19px;font-weight:700;color:var(--sky)}
.contact .mail{font-size:15px;color:var(--grey)}
.contact .web{font-size:13.5px;font-weight:700;color:var(--grey)}
.contact .web span{color:var(--orange)}

/* back */
.back-title{left:22px;top:42px;font-weight:800;line-height:1.2}
.back-title .l1{font-size:33px;color:var(--orange)}
.back-title .l1 small{font-size:20px;font-weight:600;color:#8a8f95}
.back-title .l2{font-size:20px;font-weight:600;color:#8a8f95}
.back-title .l2 b{font-size:30px;font-weight:800;color:var(--navy)}
.back-title .l2 b.sky{color:var(--sky)}
.story{left:0;top:150px;width:426px;height:660px;background:linear-gradient(180deg,var(--plum) 0%,var(--plum) 62%,#8a5a4a 72%,#d07a3a 84%,#7a4a3a 100%)}
.story-text{left:21px;top:176px;width:205px;color:var(--white);font-size:14.4px;line-height:1.26}
.story-text p{margin-bottom:18px}
.story-text strong{color:#f7c948;font-weight:700}
.strip{left:252px;top:196px;width:172px;transform:rotate(4deg);transform-origin:top left}
.strip .frame{background:var(--white);padding:5px;margin-bottom:3px;box-shadow:1px 2px 4px rgba(0,0,0,.35)}
.strip .frame div{width:100%}
.closing{left:18px;top:744px;width:395px;color:var(--white);font-size:14.2px;line-height:1.3}
.closing strong{letter-spacing:1px}
</style>
</head>
<body>

<!-- FRONT SIDE -->
<section class="card card--front">
  <div class="abs hero" role="img" aria-label="Jungle canopy photo with toucan and a rappeller on a waterfall"></div>
  <h1 class="abs hero-title"><span class="small">Seven</span><span class="big">Trail Days</span></h1>
  <svg class="abs wave" style="top:130px" width="424" height="60" viewBox="0 0 424 60" aria-hidden="true">
    <path d="M0 20 Q110 0 230 18 T424 10 V60 H0Z" fill="var(--white)"/>
    <path d="M0 20 Q110 0 230 18 T424 10 V22 Q320 30 220 28 T0 34Z" fill="var(--navy)"/>
    <path d="M0 34 Q110 26 220 30 T424 22 V28 Q320 38 220 36 T0 42Z" fill="var(--sky)"/>
  </svg>
  <div class="abs tagline">8 DAYS<span class="dot">●</span><span class="mid">8 ADVENTURES</span><span class="dot">●</span><span class="end">1 LIFE</span></div>

  <!-- row 1 -->
  <div class="tile-photo" style="left:11px;top:203px;width:130px;height:109px;background:linear-gradient(135deg,#3f7a2a,#9acb3a)" role="img" aria-label="Red-eyed tree frog"></div>
  <div class="tile-cap bg-sky" style="left:11px;top:312px;width:130px;height:55px">Pick Up San Jose International Airport</div>
  <div class="badge bg-sky" style="left:11px;top:203px">1</div>

  <div class="tile-photo" style="left:147px;top:203px;width:130px;height:109px;background:linear-gradient(135deg,#3d6f6a,#5a9aa0)" role="img" aria-label="Group kayaking on a river"></div>
  <div class="tile-cap bg-orange" style="left:147px;top:312px;width:130px;height:55px"><span>Beginner<br><b>KAYAKING</b></span></div>
  <div class="badge bg-orange" style="left:147px;top:203px">2</div>

  <div class="tile-photo" style="left:283px;top:203px;width:130px;height:109px;background:linear-gradient(135deg,#c9d6dc,#6e8a9a)" role="img" aria-label="Whitewater rafting crew"></div>
  <div class="tile-cap bg-royal" style="left:283px;top:312px;width:130px;height:55px;font-size:12.5px"><span>Whitewater <b style="font-size:12.5px">Rafting.</b> Overnight Jungle Lodge</span></div>
  <div class="badge bg-royal" style="left:283px;top:203px">3</div>

  <!-- row 2 -->
  <div class="tile-photo" style="left:11px;top:373px;width:130px;height:110px;background:linear-gradient(135deg,#2f5a22,#6a9a3a)" role="img" aria-label="Zipline through the jungle"></div>
  <div class="tile-cap small bg-orange" style="left:11px;top:483px;width:130px;height:55px"><span>Canopy/ Zipline Tour &amp; <b>Jungle Hikes.</b> Overnight Jungle Lodge</span></div>
  <div class="badge bg-orange" style="left:11px;top:373px">4</div>

  <div class="tile-photo" style="left:147px;top:373px;width:130px;height:110px;background:linear-gradient(180deg,#e0a050,#7a5030)" role="img" aria-label="Friends dancing on the beach at sunset"></div>
  <div class="tile-cap bg-royal" style="left:147px;top:483px;width:130px;height:55px"><span>Whitewater<br>Rafting &amp; <b>BEACH</b></span></div>
  <div class="badge bg-royal" style="left:147px;top:373px">5</div>

  <div class="tile-photo" style="left:283px;top:373px;width:130px;height:110px;background:linear-gradient(180deg,#3aa0c0,#14607a)" role="img" aria-label="Snorkelers underwater"></div>
  <div class="tile-cap bg-orange" style="left:283px;top:483px;width:130px;height:55px"><b>SURFING &amp;<br>SNORKELING</b></div>
  <div class="badge bg-orange" style="left:283px;top:373px">6</div>

  <!-- row 3 -->
  <div class="tile-photo" style="left:11px;top:543px;width:130px;height:109px;background:linear-gradient(135deg,#2a3a2a,#5a6a4a)" role="img" aria-label="Canyoning rappel down a rock wall"></div>
  <div class="tile-photo" style="left:147px;top:543px;width:130px;height:109px;background:linear-gradient(135deg,#4a6a3a,#b0c0b0)" role="img" aria-label="Canyoning under a waterfall"></div>
  <div class="tile-cap bg-sky" style="left:11px;top:652px;width:266px;height:54px;font-size:13px"><span><b>CANYONING</b> (Rappelling Waterfalls)<br>or Mountain Biking. Your choice!</span></div>
  <div class="badge bg-sky" style="left:11px;top:543px">7</div>

  <div class="tile-photo" style="left:283px;top:543px;width:130px;height:109px;background:linear-gradient(135deg,#5a7a3a,#a0906a)" role="img" aria-label="Sloth in a tree"></div>
  <div class="tile-cap bg-royal" style="left:283px;top:652px;width:130px;height:54px">Drop Off San Jose International Airport</div>
  <div class="badge bg-royal" style="left:283px;top:543px">8</div>

  <p class="abs pitch">Come join us in the tropics on one of our all inclusive 8 day <span class="hl">SEVEN TRAIL DAYS</span> tours.</p>

  <svg class="abs wave" style="top:788px" width="424" height="40" viewBox="0 0 424 40" aria-hidden="true">
    <path d="M0 14 Q110 4 220 14 T424 6 V16 Q320 26 220 24 T0 26Z" fill="var(--navy)"/>
    <path d="M0 26 Q110 20 220 24 T424 16 V24 Q320 34 220 32 T0 34Z" fill="var(--sky)"/>
  </svg>
  <div class="abs sticker"><span class="old">$1999</span><span class="only">ONLY</span><span class="price">$1649</span></div>

  <div class="abs" style="left:20px;top:843px"><span class="brand">PURA SENDA</span><span class="brand-dot"></span></div>
  <div class="abs contact" style="right:20px;top:842px">
    <div class="phone">1-888-555-0142</div>
    <div class="mail">info@PuraSendaTrek.example</div>
    <div class="web">www.<span>PuraSendaTrek</span>.example</div>
  </div>
</section>

<!-- BACK SIDE -->
<section class="card card--back">
  <h2 class="abs back-title"><span class="l1">HONEYMOONS <small>&amp; CUSTOM</small></span><br><span class="l2">AND <b>FAMILY</b> <b class="sky">TOURS</b></span></h2>
  <div class="abs story" role="img" aria-label="Couple walking hand in hand along the shore at sunset"></div>
  <svg class="abs wave" style="top:128px" width="426" height="40" viewBox="0 0 426 40" aria-hidden="true">
    <path d="M0 14 Q110 4 220 14 T426 6 V16 Q320 26 220 24 T0 26Z" fill="var(--navy)"/>
    <path d="M0 26 Q110 20 220 24 T426 16 V24 Q320 34 220 32 T0 34Z" fill="var(--sky)"/>
  </svg>
  <div class="abs story-text">
    <p>Pura Senda has been specializing in helping plan <strong>UNIQUE TROPICAL GETAWAYS</strong> since 1995. Based in Costa Rica 365 days a year, we are able to recommend the best activities, hotels and destinations to suit your vacation/ honeymoon desires.</p>
    <p>We have personally explored and enjoyed many of the region’s attractions and know which ones will give you the <strong>BEST EXPERIENCE</strong> while you are here.</p>
  </div>
  <div class="abs strip">
    <div class="frame"><div style="height:128px;background:linear-gradient(135deg,#f0b070,#7ac0e0)" role="img" aria-label="Kids in snorkel masks on the beach"></div></div>
    <div class="frame"><div style="height:126px;background:linear-gradient(180deg,#5ab8d8,#e8d0b0)" role="img" aria-label="Feet in the sand by the sea"></div></div>
    <div class="frame"><div style="height:250px;background:linear-gradient(180deg,#5a9ad8,#d8e8f0 30%,#3a6a2a 55%,#4ab0d8 100%)" role="img" aria-label="Jungle infinity pool with waterfall"></div></div>
  </div>
  <p class="abs closing">Let us know what you are looking for and we’ll come up with an <strong>INCREDIBLE ITINERARY</strong>, just for you!</p>
  <svg class="abs wave" style="top:790px" width="426" height="40" viewBox="0 0 426 40" aria-hidden="true">
    <path d="M0 0 H426 V6 Q320 22 220 16 T0 20Z" fill="#7a4a3a"/>
    <path d="M0 18 Q110 8 220 16 T426 6 V16 Q320 26 220 24 T0 28Z" fill="var(--navy)"/>
    <path d="M0 28 Q110 22 220 24 T426 16 V24 Q320 34 220 32 T0 36Z" fill="var(--sky)"/>
    <path d="M0 36 Q110 30 220 32 T426 24 V40 H0Z" fill="var(--white)"/>
  </svg>
  <div class="abs" style="left:20px;top:847px"><span class="brand">PURA SENDA</span><span class="brand-dot"></span></div>
  <div class="abs contact" style="right:20px;top:846px">
    <div class="phone">1-888-555-0142</div>
    <div class="mail">info@PuraSendaTrek.example</div>
    <div class="web">www.<span>PuraSendaTrek</span>.example</div>
  </div>
</section>

</body>
</html>
```